Suds Harbor Laundromat Wordpress Design

We need a Wordpress website design for our laundromat, Suds Harbor Atlanta, at www.sudsharboratlanta-example.com. We would like to have 6 pages: Home, About Us, Services, Locations, Reviews and Contact us. We will provide content for the text on each page. What we do: We are a full service laundromat that provides dry cleaning drop off, professional laundry services, wash dry fold and self service laundry to the local community. We would like to use the color scheme from our logo to convey a warm, safe, and bright business that caters to its diverse community.
Updates

I like the structure of this laundromat website: http://www.tumblewashhub-example.com/ Using my logo and color scheme in the above referenced website is what. Am looking for. The photos attached to the project with the female model should be used as a primary focus and supplemented by actual photos of the equipment.

Target Market(s)

Our target market is a diverse group of people from Midtown Atlanta - LGBTQ community /Locals/Regulars that have been coming to laundromat for 30 years.

Industry/Entity Type

Laundromat

Coding

Coded - Design and coding required

Number of Pages Required

5+ page

Font styles to use
Sans Serif

Colors
0054AA
0677BA
7BADD7
CADEEF
E8F1F8

Requirements
Must have
• Feature this video on the main page: https://video.example.com/Qx7mBr2Lp0Z

```html
<!DOCTYPE html>
<html lang="en">
<head>
<meta charset="utf-8">
<title>Contact Us – Suds Harbor</title>
<link href="https://fonts.googleapis.com/css2?family=Bebas+Neue&family=Montserrat:wght@400;500;600;700&display=swap" rel="stylesheet">
<style>
:root{
  --navy:#32476b;
  --blue:#0054aa;
  --mid:#0677ba;
  --sky:#10a0e0;
  --ink:#222;
  --line:#d9dde3;
  --white:#fff;
}
*{margin:0;padding:0;box-sizing:border-box}
html,body{width:1200px;height:2263px;overflow:hidden;background:var(--white)}
body{position:relative;font-family:'Montserrat',sans-serif;color:var(--ink)}
.abs{position:absolute}
.site-header{position:absolute;left:0;top:0;width:1200px;height:76px;background:var(--white);z-index:3}
.brand{position:absolute;left:104px;top:20px;display:flex;align-items:center;gap:8px}
.brand-dot{width:14px;height:14px;border-radius:50%;background:var(--mid)}
.brand-name{font-size:22px;font-weight:700;color:var(--mid);letter-spacing:.5px}
.main-nav a{position:absolute;top:34px;font-size:12px;color:var(--ink);text-decoration:none;letter-spacing:.2px}
.main-nav a.active{color:#000;font-weight:500}
.main-nav .bar{position:absolute;left:925px;top:71px;width:86px;height:4px;background:var(--blue)}
.nav-divider{position:absolute;left:1029px;top:18px;width:2px;height:38px;background:var(--blue)}
.social-sm{position:absolute;top:33px;width:11px;height:11px;border-radius:50%;background:#111}
.hero{position:absolute;left:0;top:76px;width:1200px;height:410px;background:linear-gradient(180deg,#c9c07a 0%,#b9b58a 40%,#d9d7cc 70%,#e8e6dd 100%)}
.hero-curve{position:absolute;left:0;top:390px;width:1200px;height:100px}
.crumb{position:absolute;left:163px;top:505px;font-size:12px;font-weight:500}
.crumb span{color:var(--mid);font-weight:600}
.page-title{position:absolute;left:0;top:596px;width:1200px;text-align:center;font-family:'Bebas Neue',sans-serif;font-size:36px;color:#2b2b2b;letter-spacing:.5px}
.page-title span{color:var(--blue)}
.title-rule{position:absolute;left:577px;top:641px;width:46px;height:3px;background:var(--sky)}
.info-panel{position:absolute;left:162px;top:742px;width:427px;height:373px;background:var(--navy);color:var(--white);font-size:14px;line-height:23px}
.info-row{position:absolute;left:52px;display:flex;gap:22px;align-items:flex-start}
.info-row svg{flex:none;margin-top:2px}
.map{position:absolute;left:589px;top:683px;width:611px;height:491px;background:linear-gradient(135deg,#eceef0,#e3e6e8 60%,#d8e8d3)}
.intro{position:absolute;left:0;width:1200px;text-align:center;font-size:15px;font-weight:500}
.intro.cta{font-size:12.5px;color:var(--blue);text-transform:uppercase;font-weight:500}
.field{position:absolute;border:1px solid var(--line);background:var(--white);font-size:11px;color:#555;padding:14px 15px}
.captcha{position:absolute;left:485px;top:1544px;width:230px;height:57px;border:1px solid #d3d3d3;background:#f9f9f9;border-radius:3px}
.captcha .box{position:absolute;left:11px;top:17px;width:22px;height:22px;border:2px solid #c1c1c1;background:#fff;border-radius:2px}
.captcha .lbl{position:absolute;left:41px;top:21px;font-size:10px;color:#222}
.captcha .mark{position:absolute;right:14px;top:10px;width:22px;height:22px;border-radius:50%;background:#4a90e2}
.captcha .small{position:absolute;right:9px;top:36px;font-size:7px;color:#666;text-align:center;line-height:9px}
.submit{position:absolute;left:539px;top:1618px;width:120px;height:42px;background:var(--sky);color:#fff;font-size:14px;font-weight:600;display:flex;align-items:center;justify-content:center}
.site-footer{position:absolute;left:0;top:1736px;width:1200px;height:527px;background:var(--navy);color:var(--white)}
.f-brand{position:absolute;left:0;top:62px;width:1200px;text-align:center}
.f-brand .name{font-family:'Bebas Neue',sans-serif;font-size:58px;letter-spacing:1px;line-height:58px}
.f-brand .tag{font-size:13px;letter-spacing:.3px}
.f-rule{position:absolute;height:1px;background:rgba(255,255,255,.15)}
.f-nav a{position:absolute;top:231px;font-size:15px;color:var(--white);text-decoration:none}
.f-social{position:absolute;top:226px;width:30px;height:30px;border-radius:50%;background:var(--white)}
.f-text{position:absolute;font-size:13.5px;line-height:24px}
.f-text.blue{color:var(--sky);font-weight:500}
.copyright{position:absolute;left:0;top:463px;width:1200px;text-align:center;font-size:12px}
.copyright b{font-weight:600}
</style>
</head>
<body>

<header class="site-header">
  <div class="brand"><span class="brand-dot"></span><span class="brand-name">Suds Harbor</span></div>
  <nav class="main-nav">
    <a style="left:416px">HOME</a>
    <a style="left:496px">ABOUT US</a>
    <a style="left:604px">SERVICES</a>
    <a style="left:708px">LOCATION</a>
    <a style="left:826px">REVIEWS</a>
    <a class="active" style="left:925px">CONTACT US</a>
    <span class="bar"></span>
  </nav>
  <span class="nav-divider"></span>
  <span class="social-sm" style="left:1048px"></span>
  <span class="social-sm" style="left:1075px"></span>
</header>

<div class="hero" role="img" aria-label="Photo of the laundromat interior with rows of front-load washers and potted plants"></div>
<svg class="hero-curve" viewBox="0 0 1200 100" preserveAspectRatio="none">
  <path d="M0 20 Q560 160 1200 20 L1200 100 L0 100 Z" fill="#fff"/>
  <path d="M0 22 Q560 150 1150 35" fill="none" stroke="#0054aa" stroke-width="14"/>
</svg>

<div class="crumb">HOME / <span>CONTACT US</span></div>

<h1 class="page-title">CONTACT <span>US</span></h1>
<div class="title-rule"></div>

<section class="info-panel">
  <div class="info-row" style="top:55px">
    <svg width="18" height="18" viewBox="0 0 20 20" fill="none" stroke="#fff" stroke-width="1.3"><circle cx="10" cy="10" r="8"/><path d="M2 10h16M10 2c3 3 3 13 0 16M10 2c-3 3-3 13 0 16"/></svg>
    <div>Harborview Plaza,<br>2210 Maple Crest Ave NE., # 118,<br>Atlanta, GA 30309</div>
  </div>
  <div class="info-row" style="top:154px">
    <svg width="18" height="18" viewBox="0 0 20 20" fill="none" stroke="#fff" stroke-width="1.3"><path d="M4 2l3 4-2 2c1 3 4 6 7 7l2-2 4 3-2 3C9 18 2 11 1 4z"/></svg>
    <div>(404) 555-0142</div>
  </div>
  <div class="info-row" style="top:206px">
    <svg width="20" height="16" viewBox="0 0 22 16" fill="none" stroke="#fff" stroke-width="1.3"><rect x="1" y="1" width="20" height="14"/><path d="M1 1l10 8 10-8M1 15l7-7M21 15l-7-7"/></svg>
    <div>hello@sudsharbor-example.com</div>
  </div>
  <div class="info-row" style="top:259px">
    <svg width="20" height="20" viewBox="0 0 20 20" fill="none" stroke="#fff" stroke-width="1.3"><circle cx="10" cy="10" r="9"/><path d="M10 4v6l4 3"/></svg>
    <div>Covid 19 hours<br>open 7 days a week 8 am to 8 pm</div>
  </div>
</section>

<div class="map" role="img" aria-label="Street map showing the laundromat location in Midtown Atlanta"></div>

<p class="intro" style="top:1257px">Would You Like To Know More About Us?</p>
<p class="intro" style="top:1292px">Have A Question About Our Services?</p>
<p class="intro cta" style="top:1331px">Please feel free to call or email us for more information.</p>

<div class="field" style="left:337px;top:1370px;width:255px;height:41px">Name*</div>
<div class="field" style="left:607px;top:1370px;width:255px;height:41px">Email*</div>
<div class="field" style="left:337px;top:1429px;width:525px;height:94px">How may we help you?</div>

<div class="captcha">
  <span class="box"></span><span class="lbl">I'm not a robot</span>
  <span class="mark"></span>
  <span class="small">Verify<br>Privacy - Terms</span>
</div>

<div class="submit">Submit</div>

<footer class="site-footer">
  <div class="f-brand">
    <div class="name">SUDS HARBOR</div>
    <div class="tag">A FULL SERVICE LAUNDROMAT</div>
  </div>
  <div class="f-rule" style="left:246px;top:199px;width:641px"></div>
  <nav class="f-nav">
    <a style="left:254px">Home</a>
    <a style="left:338px">About Us</a>
    <a style="left:446px">Services</a>
    <a style="left:549px">Location</a>
    <a style="left:659px">Reviews</a>
    <a style="left:762px">Contact Us</a>
  </nav>
  <span class="f-social" style="left:879px"></span>
  <span class="f-social" style="left:924px"></span>
  <div class="f-rule" style="left:246px;top:280px;width:641px"></div>

  <svg class="abs" style="left:246px;top:313px" width="18" height="18" viewBox="0 0 20 20" fill="none" stroke="#fff" stroke-width="1.3"><circle cx="10" cy="10" r="8"/><path d="M2 10h16M10 2c3 3 3 13 0 16M10 2c-3 3-3 13 0 16"/></svg>
  <div class="f-text" style="left:277px;top:310px">Harborview Plaza, 2210 Maple Crest<br>Ave NE., # 118, Atlanta, GA 30309</div>
  <svg class="abs" style="left:246px;top:364px" width="18" height="18" viewBox="0 0 20 20" fill="none" stroke="#fff" stroke-width="1.3"><path d="M4 2l3 4-2 2c1 3 4 6 7 7l2-2 4 3-2 3C9 18 2 11 1 4z"/></svg>
  <div class="f-text" style="left:275px;top:361px">(404) 555-0142</div>

  <div class="f-text blue" style="left:611px;top:309px">Delivery Available* <span style="font-weight:400">please contact us for details</span></div>
  <div class="f-text" style="left:611px;top:340px">Covid 19 hours - open 7 days a week 8 am to 8 pm<br>Last wash begins 6:30 pm</div>

  <div class="f-rule" style="left:162px;top:417px;width:877px"></div>
  <p class="copyright">Copyright © 2021 <b>Suds Harbor Atlanta</b>. All Rights Reserved.</p>
</footer>

</body>
</html>
```